Poster promoting the "Golden Crust Day"

The Meridan Federation of Oven Crafts (MFOC) created the "Golden Crust Day" in 2006. It is celebreated each year together with the GNX "Harvest Table Day" on 16th October.
After using different posters for a few years, MFOC decided to settle on a permanent poster some time ago, in order to allow people to recognize the poster long-term.
Now, MFOC feels that this permanent poster needs an update and modernization, apart from including the new MFOC logo.
Requisits:
1. Must include the new MFOC logo
2. The poster should reflect the importance of bread in the world and convey an image of health, innovation and tradition.
3. One version with text, one version without text
4. Text version: one poster for each of the four official MFOC languages:
ENGLISH: Golden Crust Day / 16th October
GERMAN: Goldkrustentag / 16. Oktober
SPANISH: Día de la Corteza Dorada / 16 de Octubre
FRENCH: Journée de la Croûte Dorée / 16 Octobre
5. Colours must be defined with RGB colour code.
MFOC will take a decision regarding the new poster design during the next meeting of its Marketing Commission on March 24th, 2015. Therefore, please submit your proposals by 18th March in order to allow for pre-selection and modification requests.
More about MFOC at www.meridanovencrafts.org.

```html
<!DOCTYPE html>
<html lang="en">
<head>
<meta charset="utf-8">
<title>Golden Crust Day – 16th October</title>
<link rel="stylesheet" href="https://fonts.googleapis.com/css2?family=Marcellus&family=Lobster&family=Open+Sans:wght@700&display=swap">
<style>
  :root {
    --paper-light: #fefdf0;
    --paper-mid: #faf6d8;
    --paper-edge: #f1eabb;
    --slice-light: #cf7a26;
    --slice-main: #b8621a;
    --slice-dark: #9a3c14;
    --title-white: #ffffff;
    --date-red: #8a1414;
    --crust-light: #c99a6a;
    --crust-dark: #8f6238;
    --ink: #1a1a1a;
    --mark-brown: #7a4a2a;
  }
  html, body {
    margin: 0;
    padding: 0;
    width: 849px;
    height: 1200px;
    overflow: hidden;
  }
  .poster {
    position: relative;
    width: 849px;
    height: 1200px;
    overflow: hidden;
    background: radial-gradient(ellipse 70% 60% at 50% 48%, var(--paper-light) 0%, var(--paper-mid) 55%, var(--paper-edge) 100%);
  }
  .slice-art {
    position: absolute;
    left: 173px;
    top: 213px;
    width: 494px;
    height: 614px;
    background: linear-gradient(160deg, var(--slice-light) 0%, var(--slice-main) 55%, var(--slice-dark) 100%);
  }
  .title {
    position: absolute;
    left: 173px;
    width: 494px;
    top: 350px;
    margin: 0;
    text-align: center;
    font-family: "Marcellus", serif;
    font-weight: 400;
    font-size: 118px;
    line-height: 112px;
    color: var(--title-white);
    letter-spacing: -1px;
  }
  .date {
    position: absolute;
    left: 273px;
    width: 298px;
    top: 858px;
    margin: 0;
    padding-bottom: 4px;
    text-align: center;
    font-family: "Lobster", cursive;
    font-size: 44px;
    line-height: 50px;
    color: var(--date-red);
    border-bottom: 3px solid var(--date-red);
  }
  .date sup {
    font-size: 26px;
    line-height: 0;
    vertical-align: 16px;
  }
  .loaf-photo {
    position: absolute;
    left: 0;
    top: 0;
  }
  .federation-mark {
    position: absolute;
    left: 0;
    width: 849px;
    top: 1042px;
    display: flex;
    justify-content: center;
    align-items: center;
    gap: 16px;
  }
  .federation-mark .dot {
    width: 34px;
    height: 34px;
    border-radius: 50%;
    background: var(--mark-brown);
  }
  .federation-mark .name {
    font-family: "Open Sans", sans-serif;
    font-weight: 700;
    font-size: 64px;
    line-height: 1;
    color: var(--mark-brown);
    letter-spacing: 2px;
  }
  .federation-name {
    position: absolute;
    left: 0;
    width: 849px;
    top: 1156px;
    margin: 0;
    text-align: center;
    font-family: "Open Sans", sans-serif;
    font-weight: 700;
    font-size: 21px;
    line-height: 28px;
    color: var(--ink);
  }
</style>
</head>
<body>
<main class="poster">
  <div class="slice-art" role="img" aria-label="Painted illustration of a bread slice in warm brown brush strokes"></div>

  <h1 class="title">Golden<br>Crust<br>Day</h1>

  <p class="date">16<sup>th</sup> October</p>

  <svg class="loaf-photo" width="849" height="1200" viewBox="0 0 849 1200" role="img" aria-label="Photograph of a round crusty wholegrain loaf rising from the bottom edge">
    <defs>
      <radialGradient id="loaf-fill" cx="0.5" cy="0.2" r="0.8">
        <stop offset="0" stop-color="var(--crust-light)"/>
        <stop offset="1" stop-color="var(--crust-dark)"/>
      </radialGradient>
    </defs>
    <path d="M14 1200 C40 1060 220 998 424 998 C628 998 808 1060 836 1200 Z" fill="url(#loaf-fill)"/>
  </svg>

  <div class="federation-mark">
    <span class="dot"></span>
    <span class="name">MFOC</span>
  </div>

  <p class="federation-name">The Meridan Federation of Oven Crafts</p>
</main>
</body>
</html>
```